Web Design Project

Revamp current website adding newly designed logo and creating layout that is good on desktops, tablets, and cell phones.

Current website can be viewed at www.venkirainteriors.com

Will you see the website is small but graphics heavy in the gallery. The gallery needs to be setup so that it is easy to maintain the links and update the photos.

Needs to have high visual impact.

I need a new logo and website layout designed for my partner's business. This is a birthday present. His business is interior painting, wallpapering and design. He also has access to a wide variety of products including carpet, fabrics, furniture, wallpaper, tile, countertops, etc. I have attached some screen shots of his website for reference. He is a one man shop and has a stellar reputation with his customers. He is on-time, very tidy, excellent with animals, and always finishes on time and on budget. There are no restrictions on colors or fonts. The logo needs to work well with the website, business cards and printed materials. The website needs to flow content for device size so it looks just as good on a cell phone or tablet as it does on a desktop computer. Whatever the heck that's called! Thanks. I am looking forward to seeing everyone's ideas.

Target Market(s)

Consumers looking for interior design, painting, and wallpapering as well as interior products such as flooring, window treatments, reupholstering, counter tops, etc.

Industry/Entity Type

Cell Phone

Requirements
Must have
• Clean, sharp, visual impact (at least on the home page)
Should not have
• Clutter.

```html
<!DOCTYPE html>
<html lang="en">
<head>
<meta charset="utf-8">
<title>Venkira Interior Designs</title>
<link href="https://fonts.googleapis.com/css2?family=Kaushan+Script&family=Open+Sans:wght@400;600&family=Roboto:wght@400;500&display=swap" rel="stylesheet">
<style>
:root{
  --page:#4a4540;
  --ink:#333;
  --muted:#8a8a8a;
  --red:#b5121b;
  --green:#2ebd7a;
  --orange:#ffa200;
  --nav:#2e2e2e;
  --footer:#1e1e1e;
  --panel:#e8e8e8;
  --soft:#f5f5f5;
  --blue:#1a8ad0;
}
*{margin:0;padding:0;box-sizing:border-box}
html,body{width:783px;height:1200px;overflow:hidden}
body{background:var(--page);font-family:"Open Sans",sans-serif;color:var(--ink);position:relative}
.site{position:absolute;left:113px;top:12px;width:558px;height:1158px;background:#fff}
.header{height:71px;position:relative}
.brand{position:absolute;left:17px;top:22px;font-family:"Roboto",sans-serif;font-weight:500;font-size:22px;color:var(--red);letter-spacing:.2px}
.call{position:absolute;left:329px;top:32px;font-family:"Roboto",sans-serif;font-size:12px;color:#444}
.call span{color:var(--blue)}
.social{position:absolute;left:483px;top:30px;display:flex;gap:4px}
.social i{width:16px;height:16px;border-radius:50%;display:block}
.nav{position:absolute;left:-4px;top:71px;width:566px;height:35px;background:var(--nav);display:flex}
.nav a{font-family:"Roboto",sans-serif;font-size:11px;color:#fff;text-decoration:none;height:35px;line-height:35px;padding:0 20px;border-right:1px solid #3c3c3c}
.slider{position:absolute;left:0;top:106px;width:558px;height:384px;background:var(--panel)}
.hero{position:absolute;left:13px;top:18px;width:532px;height:262px;background:linear-gradient(160deg,#e6e1d8 0%,#cbc3b6 45%,#6f6a66 80%,#3a3836 100%)}
.caption{position:absolute;left:0;bottom:0;width:100%;height:59px;background:rgba(30,30,30,.72);color:#fff;padding:6px 18px}
.caption h2{font-family:"Kaushan Script",cursive;font-weight:400;font-size:22px;line-height:28px}
.caption p{font-size:7.5px;margin-top:3px;white-space:nowrap}
.thumbs{position:absolute;left:39px;top:308px;display:flex;gap:14px}
.thumbs div{width:85px;height:71px;border:3px solid #fff;background:linear-gradient(160deg,#e9e4dc,#b9ad9d)}
.arrow{position:absolute;width:12px;height:12px;border-radius:50%;background:#fff;border:1px solid #ddd;font-size:8px;line-height:10px;text-align:center;color:#777}
.services{position:absolute;top:518px;left:13px;display:flex;gap:15px}
.svc{width:167px;height:98px;color:#fff;position:relative;padding:9px 8px 0 64px}
.svc h3{font-family:"Kaushan Script",cursive;font-weight:400;font-size:15px;line-height:22px;white-space:nowrap;letter-spacing:-.2px}
.svc p{font-size:7px;line-height:12px;margin-top:4px;text-align:justify}
.svc .more{font-size:7.5px;margin-top:8px;display:block}
.svc svg{position:absolute;left:13px;top:32px}
.green{background:var(--green)}.orange{background:var(--orange)}.red{background:var(--red)}
.products{position:absolute;top:641px;left:0;width:558px;height:231px;background:var(--soft)}
.section-title{font-family:"Roboto",sans-serif;font-size:15px;color:var(--red);position:absolute;left:13px;top:20px}
.cards{position:absolute;left:13px;top:41px;display:flex;gap:15px}
.card{width:167px;height:168px;background:#fff;border:1px solid #e6e6e6}
.card .img{height:101px}
.card h4{font-family:"Kaushan Script",cursive;font-weight:400;font-size:17px;color:var(--red);padding:7px 9px 0}
.card p{font-size:7px;color:var(--muted);line-height:13px;padding:2px 28px 0 9px}
.card .arrow{position:relative;float:right;margin:-19px 9px 0 0}
.welcome{position:absolute;top:872px;left:0;width:558px;height:228px}
.welcome-title{font-family:"Kaushan Script",cursive;font-weight:400;font-size:16px;color:#444;position:absolute;left:13px;top:26px}
.welcome-title span{color:var(--red)}
.welcome-photo{position:absolute;left:13px;top:67px;width:150px;height:142px;background:linear-gradient(170deg,#ece6dc,#c7b8a2 60%,#8d6a48)}
.welcome-sub{position:absolute;left:179px;top:66px;font-family:"Roboto",sans-serif;font-weight:400;font-size:13.5px;line-height:18px;color:#555}
.welcome-text{position:absolute;left:179px;top:114px;width:187px;font-size:7px;line-height:13.5px;color:#777;text-align:justify}
.news-title{position:absolute;left:378px;top:20px;font-family:"Kaushan Script",cursive;font-size:16px;color:#555;width:168px;border-bottom:1px solid #eee;padding-bottom:5px}
.news{position:absolute;left:378px;width:168px;height:62px}
.date{position:absolute;left:0;top:0;width:24px;height:41px;background:var(--red);color:#fff;text-align:center;font-family:"Roboto",sans-serif}
.date b{display:block;font-size:12px;font-weight:500;padding-top:4px}
.date small{font-size:7.5px}
.date::after{content:"";position:absolute;right:-5px;top:8px;border:5px solid transparent;border-left-color:var(--red);border-right:0}
.chat{position:absolute;left:0;top:41px;width:24px;height:19px;background:#777}
.news-head{font-family:"Roboto",sans-serif;font-weight:400;font-size:10.5px;color:#777;margin-left:41px}
.news-body{font-size:7px;line-height:12.5px;color:#999;margin:7px 0 0 41px;text-align:justify}
.footer{position:absolute;left:0;top:1100px;width:558px;height:58px;background:var(--footer);color:#ddd}
.footer .copy{position:absolute;left:13px;top:14px;font-size:7.5px}
.footer .links{position:absolute;left:13px;top:39px;font-size:6.5px}
.footer .icons{position:absolute;left:292px;top:25px;display:flex;gap:6px}
.footer .icons i{width:16px;height:16px;border:1px solid #666;border-radius:50%;display:block}
.footer .addr{position:absolute;left:419px;top:17px;font-size:6.5px}
.footer .phone{position:absolute;left:419px;top:37px;font-size:10px;font-family:"Roboto",sans-serif}
</style>
</head>
<body>
<div class="site">
  <header class="header">
    <div class="brand">Venkira Interior Designs</div>
    <div class="call">Call Us : <span>+1 800 555 0147</span></div>
    <div class="social"><i style="background:#3b5998"></i><i style="background:#1da1f2"></i><i style="background:#d9312b"></i></div>
  </header>
  <nav class="nav"><a>Home</a><a>About Us</a><a>Gallery</a><a>Products</a><a>Services</a><a>Contact Us</a></nav>

  <section class="slider">
    <div class="hero" role="img" aria-label="Bright living room with sofa, floor lamp and home office desk">
      <div class="caption"><h2>Interior Designs</h2><p>With the various materials, colors, and finishes available the choices today can be daunting. By listening to you, I am able to pick just</p></div>
    </div>
    <div class="arrow" style="left:2px;top:336px">‹</div>
    <div class="thumbs">
      <div role="img" aria-label="Living room thumbnail"></div>
      <div role="img" aria-label="White lounge thumbnail"></div>
      <div role="img" aria-label="Curtained room thumbnail"></div>
      <div role="img" aria-label="Dining area thumbnail"></div>
      <div role="img" aria-label="Dining table thumbnail"></div>
    </div>
    <div class="arrow" style="left:545px;top:336px">›</div>
  </section>

  <section class="services">
    <div class="svc green">
      <svg width="36" height="44" viewBox="0 0 36 44"><rect x="4" y="2" width="26" height="9" rx="2" fill="#fff"/><path d="M30 6h3v12H19v6" stroke="#fff" stroke-width="2" fill="none"/><rect x="16" y="24" width="7" height="16" rx="2" fill="#fff"/></svg>
      <h3>Interior Painting</h3><p>At vero eos et accusamus et iusto odio dignissimos ducimus qui</p><span class="more">Read More</span>
    </div>
    <div class="svc orange">
      <svg width="36" height="44" viewBox="0 0 36 44"><path d="M6 8q14-8 26 0v22q-12-6-26 8z" fill="#fff"/></svg>
      <h3>Wallpapering</h3><p>At vero eos et accusamus et iusto odio dignissimos ducimus qui</p><span class="more">Read More</span>
    </div>
    <div class="svc red">
      <svg width="44" height="40" viewBox="0 0 44 40"><rect x="14" y="2" width="16" height="36" fill="#fff"/><rect x="2" y="14" width="12" height="24" fill="#fff"/><rect x="30" y="14" width="12" height="24" fill="#fff"/><path d="M18 8h8M18 14h8M18 20h8M18 26h8M5 20h6M5 26h6M33 20h6M33 26h6" stroke="#b5121b" stroke-width="2"/></svg>
      <h3>Design</h3><p>At vero eos et accusamus et iusto odio dignissimos ducimus qui</p><span class="more">Read More</span>
    </div>
  </section>

  <section class="products">
    <div class="section-title">Products</div>
    <div class="arrow" style="left:516px;top:21px">‹</div><div class="arrow" style="left:533px;top:21px">›</div>
    <div class="cards">
      <div class="card"><div class="img" role="img" aria-label="Rolled carpets" style="background:linear-gradient(160deg,#d8cbb8,#9c8067 55%,#a52a22)"></div><h4>Carpet</h4><p>Lorem ipsum dolor sit amet, eiusmod tempor incididunt</p><div class="arrow">›</div></div>
      <div class="card"><div class="img" role="img" aria-label="Kitchen with wooden countertop" style="background:linear-gradient(170deg,#e9e6e0,#b9b2a8 50%,#5a3322)"></div><h4>Countertops</h4><p>Lorem ipsum dolor sit amet, eiusmod tempor incididunt</p><div class="arrow">›</div></div>
      <div class="card"><div class="img" role="img" aria-label="Living room furniture" style="background:linear-gradient(170deg,#e6dccb,#b08a64 55%,#8a4a22)"></div><h4>Furniture</h4><p>Lorem ipsum dolor sit amet, eiusmod tempor incididunt</p><div class="arrow">›</div></div>
    </div>
  </section>

  <section class="welcome">
    <h2 class="welcome-title">Welcome To <span>Venkira Interior Designs</span></h2>
    <div class="welcome-photo" role="img" aria-label="Room with wooden bench, framed pictures and sofa"></div>
    <h3 class="welcome-sub">To Our Interior Designs<br>Maintenance</h3>
    <p class="welcome-text">With the various materials, colors, and finishes available the choices today can be daunting. By listening to you, I am able to pick just the right color, the right fabric, or the right furniture for your projects. Whether you are starting with a small project or a large project, I am ready to bring your ideas to life. It doesn't take a big budget to achieve dramatic effects. A wonderful new look is within anyone's reach.</p>
    <div class="news-title">Latest News</div>
    <div class="news" style="top:67px"><div class="date"><b>15</b><small>Sep</small></div><div class="chat"></div><h5 class="news-head">Mes cuml dia sed in lacus</h5><p class="news-body">Morbi tempor quam vel massa adi piscing ute cursus mi congue pelle ntesque niselit er comte</p></div>
    <div class="news" style="top:146px"><div class="date"><b>15</b><small>Sep</small></div><div class="chat"></div><h5 class="news-head">Mes cuml dia sed in lacus</h5><p class="news-body">Morbi tempor quam vel massa adi piscing ute cursus mi congue pelle ntesque niselit er comte</p></div>
  </section>

  <footer class="footer">
    <div class="copy">©2014 Venkira Interior Designs , All Rights Reserved.</div>
    <div class="links">Home | About | Services | Products | Gallery | Contact</div>
    <div class="icons"><i></i><i></i><i></i></div>
    <div class="addr">4820 W Larkspur Ln. • Fairmont, KS 66990</div>
    <div class="phone">Phone: (913) 555-0182</div>
  </footer>
</div>
</body>
</html>
```